Wine Label Design-Crimson Gully Vineyard

Crimson Gully Vineyard is in the Barossa Valley in South Australia. The Barossa is recognized as Australia's premier wine region, producing Australia's icon wines and some " new takes on traditional".
This family owned and operated vineyard grows some exceptionally high quality fruit. Most of the fruit is sold and used for some of Australia's most iconic wines. Small quantities are retained by the owners for some wines with very limited availability. (Wines were previously sold as Pellow Draycott Vineyards Crimson Gully ( Shiraz, Cabernet etc).

The wines will in the future be labeled simply ‘Crimson Gully Vineyard’. The label will launch this new identity for the single family single vineyard and its high quality wines which are a true expression of the vineyard and derive from the Crimson Gully common to this ancient area (800-2000 million years old).
The label should reflect
• Single vineyard, family owned
• vines in very old rock & soils
• High quality & reliability
• Edgy but true, design based thinking (Please note:blue is generally seen as an unacceptable colour for a wine label?? Don’t ask me why)

The wines will be sold mostly direct in Australia ( ie not through retail stores), with limited export to Asia, Scandinavia and Canada.
There are three quality levels and price points in the portfolio
1. Entry level premium for everyday drinking for discriminating drinkers-approx AUD20
2. Super Premium-approx AUD30
3. Limited Release ultlra premium-AUD75-90?
We envisage three variations on the label but with an obvious & common design element. This design element should be able to be used for corporate identification and promotion
The paper stock will be waterproof and self adhesive. Our preference is for designs that engage the user by appealing to both sight and touch. It is preferred that textures be added eg embossing, high build varnish etc-rather than be a facet of the stock itself.
For information on statutory label requirements refer to www.vintnerregistry-example.com . In brief
o Front label need not show any mandatory information. However we would prefer Variety, Barossa Valley, Year and alcohol to be shown on the front label
o Back label should show all mandatories and allow for a bar code

Project Deadline Extended
Reason: I've had a problem with my wireless broadband account and reception has been intermittent to say the least to the extent that I switched off at the weekend. Just going downtown now for a 'polite discussion' with my service provider.

Project Deadline Extended
Reason: I have receiver insufficient designs of quality which we would consider. Too many designs have a "cut and paste" appearance - too few exhibit an original art/design element which truly identifies the product.

Gals & Guys

most of the designs submitted lack punch and originality and are totally unmemorable.
Please-get on Google or whatever enter "Wine Label Designs" and do some research b4 u waste your time and mine. Formulaic cut and paste will not win the day. That's not to say that cut and paste can't work-but it must have some originality, impact and command attention. Please surprise me.

Following on from a question from a designer about who is our competition and what we are looking for I sent the following 
"I don't think I can add anything new. Read the brief and comments again and research wine labels on the web. In 30 minutes you'll get a good idea of the creative edgy designs in the industry. There are a plethora of collections. Our competition-anyone with a label. In 2010 there were over 2400 "producers" in other words 2400 producers with at least one label. In fact there are over 25000 Australian wines and then the numerous imported wines.

Target Market(s)

$20 people who budget everyday but have graduated from drinking 'entry level' wines. These people will likely fit into Cat. (b) in the $30 wine

$30 (a) will not over-compromise on some everyday discretionary expenditure.(b) might buy for special occasions

$70-$90 Professional/successful people with high disposable/discretionary income not particularly worried about recession. wine geeks.

Industry/Entity Type

Retail

Requirements
Must have
• identifiable element across range of wines

```html
<!DOCTYPE html>
<html lang="en">
<head>
<meta charset="utf-8">
<title>Crimson Gully Vineyard – Barossa Valley Shiraz Label</title>
<link href="https://fonts.googleapis.com/css2?family=Archivo:wght@700&family=Noto+Serif+Display:wdth,wght@70,700&display=swap" rel="stylesheet">
<style>
  :root {
    --page: #ffffff;
    --gold: #b9a05c;
    --cream: #e1d4b5;
    --charcoal: #414141;
    --ink: #1e1e1e;
  }
  html, body {
    margin: 0;
    width: 1200px;
    height: 900px;
    overflow: hidden;
    background: var(--page);
  }
  .label {
    position: absolute;
    left: 363px;
    top: 55px;
    width: 490px;
    height: 737px;
    background: var(--gold);
    box-shadow: 4px 5px 8px rgba(0, 0, 0, 0.18);
  }
  .emblem-area {
    position: absolute;
    left: 10px;
    top: 28px;
    width: 450px;
    height: 512px;
    border-radius: 50%;
    background: radial-gradient(ellipse at 52% 48%,
      var(--charcoal) 0%, var(--charcoal) 38%,
      var(--cream) 62%, rgba(225, 212, 181, 0.6) 78%, rgba(225, 212, 181, 0) 100%);
  }
  .brand-name {
    position: absolute;
    left: 0;
    right: 0;
    top: 296px;
    margin: 0;
    text-align: center;
    font-family: "Archivo", Arial, sans-serif;
    font-weight: 700;
    font-size: 17px;
    letter-spacing: 0.2px;
    color: var(--cream);
  }
  .estate-note {
    position: absolute;
    right: 16px;
    top: 554px;
    margin: 0;
    font-family: "Noto Serif Display", "Times New Roman", serif;
    font-stretch: 70%;
    font-weight: 700;
    font-size: 21px;
    color: var(--cream);
  }
  .details-band {
    position: absolute;
    left: 0;
    right: 0;
    top: 591px;
    bottom: 0;
    background: var(--cream);
  }
  .wine-details {
    margin: 6px 0 0;
    text-align: center;
    font-family: "Noto Serif Display", "Times New Roman", serif;
    font-stretch: 70%;
    font-weight: 700;
    font-size: 27px;
    line-height: 36px;
    color: var(--charcoal);
  }
  .legal-line {
    position: absolute;
    left: 15px;
    right: 18px;
    bottom: 17px;
    display: flex;
    justify-content: space-between;
    font-family: "Noto Serif Display", "Times New Roman", serif;
    font-stretch: 70%;
    font-weight: 700;
    font-size: 16px;
    color: var(--ink);
  }
</style>
</head>
<body>
  <main class="label">
    <div class="emblem-area" role="img" aria-label="Space for the vineyard emblem: a shattered stone burst in charcoal over cream"></div>
    <h1 class="brand-name">CRIMSON GULLY VINEYARD</h1>
    <p class="estate-note">Single Estate</p>
    <section class="details-band">
      <p class="wine-details">BAROSSA VALLEY<br>SHIRAZ<br>2012</p>
      <div class="legal-line">
        <span class="volume">75cl / 25.4fl oz</span>
        <span class="alcohol">13.5% AlcVol</span>
      </div>
    </section>
  </main>
</body>
</html>
```